Lanternfield Disability - Social Security Disability Attorneys

Our company is expanding to attract clients nationwide for our social security disability practice. We have a logo, but I am looking for a creative and elegant letterhead that projects an image of being technologically advanced but still professional enough for the legal field. I am looking for the "wow factor" combined with this is still professional enough for a law practice.

Requesting letterhead and business card design
Updates

Had to update and change the logo. The previous logo had a typo. Please send updates with the new logo for consideration. The letterhead and business cards should be professional enough to be used for a law firm. Thanks.

Industry/Entity Type

Law Practice, Law Firm, Healthcare Industry, Government

Colors

Designer to choose colors to be used in the design.

Requirements
Nice to have
• **Please create a vertical design for the business card**

```html
<!DOCTYPE html>
<html lang="en">
<head>
<meta charset="utf-8">
<title>Lanternfield Disability – Stationery</title>
<link href="https://fonts.googleapis.com/css2?family=Source+Sans+3:wght@400;600&display=swap" rel="stylesheet">
<style>
  :root {
    --bg: #e8e8e8;
    --paper: #f6f9fc;
    --card-white: #f8f9fd;
    --navy: #262c40;
    --blue: #3f63d8;
    --orange: #ef7d22;
    --ink: #2a2d33;
    --sig: #dfe3ea;
  }
  * { margin: 0; padding: 0; box-sizing: border-box; }
  html, body { width: 1200px; height: 801px; overflow: hidden; background: var(--bg); }
  body {
    position: relative;
    font-family: "Source Sans 3", Arial, sans-serif;
    color: var(--ink);
    -webkit-font-smoothing: antialiased;
    -moz-osx-font-smoothing: grayscale;
  }

  /* Letterhead */
  .letterhead {
    position: absolute; left: 250px; top: 102px; width: 432px; height: 610px;
    background: var(--paper); box-shadow: 0 1px 4px rgba(0,0,0,.12);
  }
  .brand { position: absolute; left: 31px; top: 64px; width: 175px; text-align: center; color: var(--blue); }
  .brand-name { font-weight: 600; font-size: 14px; letter-spacing: .8px; white-space: nowrap; text-transform: uppercase; }
  .brand-tag { font-weight: 600; font-size: 4.6px; letter-spacing: 1.1px; margin-top: 1px; white-space: nowrap; text-transform: uppercase; }
  .contact { position: absolute; left: 296px; top: 38px; list-style: none; font-size: 6.8px; line-height: 10px; color: var(--ink); }
  .contact li { display: flex; gap: 6px; margin-bottom: 1px; }
  .contact li.gap { margin-top: 3px; }
  .contact svg { width: 7px; height: 7px; flex: none; margin-top: 1.5px; }
  .contact b { font-weight: 600; }
  .rule { position: absolute; left: 31px; top: 110px; width: 373px; height: 2px; background: var(--blue); }
  .body { position: absolute; left: 51px; top: 213px; width: 342px; font-size: 7.8px; line-height: 12px; color: var(--ink); font-weight: 400; }
  .body p { margin-bottom: 12px; }
  .closing { position: absolute; left: 339px; top: 454px; font-size: 7.8px; color: var(--ink); }
  .signature { position: absolute; left: 320px; top: 468px; width: 60px; height: 24px; background: var(--sig); border-radius: 3px; }

  /* Business cards */
  .card { position: absolute; left: 778px; width: 258px; height: 147px; box-shadow: 0 1px 4px rgba(0,0,0,.15); overflow: hidden; }
  .card-back { top: 187px; background: var(--navy); }
  .card-front { top: 401px; background: var(--card-white); }
  .card-frame { position: absolute; left: 0; top: 147px; width: 147px; height: 258px; transform-origin: top left; transform: rotate(-90deg); }

  .back-brand { position: absolute; left: 0; width: 147px; top: 102px; text-align: center; color: var(--blue); }
  .back-brand .brand-name { font-size: 9.5px; letter-spacing: .5px; }
  .back-brand .brand-tag { font-size: 3px; letter-spacing: .7px; margin-top: 1px; }
  .back-dot { position: absolute; left: 69px; top: 82px; width: 9px; height: 9px; border-radius: 50%; background: var(--orange); }

  .front-dot { position: absolute; left: 58px; top: 44px; width: 30px; height: 30px; border-radius: 50%; background: var(--orange); }
  .person { position: absolute; left: 19px; top: 122px; color: var(--blue); }
  .person-name { font-weight: 600; font-size: 11px; letter-spacing: .3px; white-space: nowrap; text-transform: uppercase; }
  .person-title { font-size: 7.2px; font-weight: 600; margin-top: 0; }
  .card-contact { position: absolute; left: 19px; top: 161px; list-style: none; font-size: 6px; line-height: 11px; color: var(--ink); }
  .card-contact li { display: flex; gap: 5px; white-space: nowrap; }
  .card-contact li.gap { margin-top: 2px; }
  .card-contact svg { width: 6px; height: 6px; flex: none; margin-top: 2.5px; }
  .card-contact b { font-weight: 600; }
</style>
</head>
<body>

<section class="letterhead">
  <div class="brand">
    <div class="brand-name">Lanternfield Disability</div>
    <div class="brand-tag">Social Security Disability Attorneys</div>
  </div>
  <ul class="contact">
    <li><svg viewBox="0 0 10 10"><path d="M2 1l2 2-1 1.5c.8 1.5 1.7 2.4 3 3L7.5 6l2 2-1.5 1.5C4.5 9 1 5.5.5 2.5z" fill="none" stroke="var(--orange)" stroke-width="1"/></svg>555.014.2290</li>
    <li><svg viewBox="0 0 10 10"><rect x=".5" y="2" width="9" height="6" fill="none" stroke="var(--orange)"/><path d="M.5 2L5 5.5 9.5 2" fill="none" stroke="var(--orange)"/></svg>Dan.Marsh@lanternfield.com</li>
    <li class="gap"><svg viewBox="0 0 10 10"><circle cx="5" cy="3.5" r="2.3" fill="none" stroke="var(--orange)"/><path d="M1 9.5c.5-2.5 7.5-2.5 8 0" fill="none" stroke="var(--orange)"/></svg><span>42 Ashgrove Lane, Suite 300<br>Elmwood, FL 32000</span></li>
    <li class="gap"><svg viewBox="0 0 10 10"><circle cx="5" cy="5" r="4.3" fill="none" stroke="var(--orange)"/><path d="M.7 5h8.6M5 .7c-2.4 2.5-2.4 6.1 0 8.6M5 .7c2.4 2.5 2.4 6.1 0 8.6" fill="none" stroke="var(--orange)" stroke-width=".8"/></svg><span>www.<b>LANTERNFIELD</b>.com</span></li>
  </ul>
  <div class="rule"></div>

  <div class="body">
    <p>Lorem ipsum dolor sit amet, consectetur adipiscing elit. Donec orci purus, luctus vitae dignissim eu, iaculis sed purus. Vivamus faucibus, ipsum nec aliquet viverra, leo mauris condimentum ligula, sit amet sagittis enim ligula quis arcu. Nam egestas tortor id nisi porttitor mattis. In tortor ante, ultricies in suscipit a, tempus non massa. Vivamus et auctor mi. Fusce vel massa nulla. Phasellus nec eros mauris, et scelerisque orci.</p>
    <p>Donec malesuada orci vitae nulla accumsan porta a id massa. Quisque accumsan iaculis magna sit amet fringilla. Maecenas consequat, magna eget tincidunt semper, odio nibh rutrum mi, id feugiat ante nisi eu risus. Vestibulum nunc orci, rhoncus a placerat in, ultricies in mi. Cras mattis varius eros, vel fringilla nisi suscipit eget. Quisque scelerisque sagittis nulla at porttitor.</p>
    <p>Sed id augue vitae urna euismod commodo aliquet a quam. Pellentesque arcu velit, cursus et malesuada ut, consequat et diam. Nullam erat sem, rhoncus id ullamcorper vitae, rhoncus et arcu. In ultricies ultricies nulla, ut rutrum nisi iaculis at. Donec eu magna a metus ornare faucibus. Fusce aliquet faucibus ultricies. Morbi semper, est id tincidunt gravida, sem arcu adipiscing lacus, ac bibendum nulla leo eu purus. Quisque nec diam sed risus consectetur a ccumsan quis quis nibh. Vestibulum id purus lorem.</p>
  </div>
  <div class="closing">Sincerely,</div>
  <div class="signature" role="img" aria-label="Handwritten signature"></div>
</section>

<section class="card card-back">
  <div class="card-frame">
    <div class="back-dot"></div>
    <div class="back-brand">
      <div class="brand-name">Lanternfield Disability</div>
      <div class="brand-tag">Social Security Disability Attorneys</div>
    </div>
  </div>
</section>

<section class="card card-front">
  <div class="card-frame">
    <div class="front-dot"></div>
    <div class="person">
      <div class="person-name">Daniel Marsh</div>
      <div class="person-title">Senior Vice president</div>
    </div>
    <ul class="card-contact">
      <li><svg viewBox="0 0 10 10"><rect x="2.5" y=".5" width="5" height="9" rx="1" fill="none" stroke="var(--orange)"/></svg>555.018.3364</li>
      <li><svg viewBox="0 0 10 10"><path d="M2 1l2 2-1 1.5c.8 1.5 1.7 2.4 3 3L7.5 6l2 2-1.5 1.5C4.5 9 1 5.5.5 2.5z" fill="none" stroke="var(--orange)"/></svg>555.014.2290</li>
      <li><svg viewBox="0 0 10 10"><rect x=".5" y="2" width="9" height="6" fill="none" stroke="var(--orange)"/><path d="M.5 2L5 5.5 9.5 2" fill="none" stroke="var(--orange)"/></svg>Dan.Marsh@lanternfield.com</li>
      <li class="gap"><svg viewBox="0 0 10 10"><circle cx="5" cy="5" r="4.3" fill="none" stroke="var(--orange)"/><path d="M.7 5h8.6M5 .7c-2.4 2.5-2.4 6.1 0 8.6M5 .7c2.4 2.5 2.4 6.1 0 8.6" fill="none" stroke="var(--orange)" stroke-width=".8"/></svg><span>www.<b>LANTERNFIELD</b>.com</span></li>
      <li class="gap"><svg viewBox="0 0 10 10"><path d="M5 9.5C2 6 1.5 4.8 1.5 3.5a3.5 3.5 0 017 0c0 1.3-.5 2.5-3.5 6z" fill="none" stroke="var(--orange)"/></svg><span>42 Ashgrove Lane, Suite 300<br>Elmwood, FL 32000</span></li>
    </ul>
  </div>
</section>

</body>
</html>
```